Brickpress Design for a website design company

Web Design for a Web Design Company - As odd as that sounds, it is exactly right. We are a website design company with over 120 regular clients, we want to redesign our current website and take it to the next level. The problem we are finding is that we are too "inside the box". Which is why we are looking outside for a designer that will take us to the next level. We need this design to look STATE OF THE ART! Obviously there is allot we can do internally once we have a completed design to wrap up the project. So what we are looking for are some design concepts based on some ideas that we will provide. Once the concept is finalized we will need the layered design and any graphics that were used in separate files. If you have any questions please send them to us privately.

Example websites of how we want to look are:

1. http://www.brivlo.example
2. http://www.plumtavern.example
3. http://zelvaworks.example
4. http://www.kup.example
5. http://www.tarnleaf.example

Our current website we are redesigning is: www.frostlanewd.example

Navigation / Pages for new website are as follows:

Home
Services (page with broad detailing)
Portfolio
RFQ
Testimonials
About
Contact

Website Design
Website Re-design
Ecommerce
Mobile Websites
Copywriting
Hosting and Maintenance
Content Marketing
Pay Per Click Marketing
Mobile Text Marketing
Local Search Marketing

Design must be brickpress compatible, we use the meridian framework specifically.
Target Market(s)
Our target market is B2B, we want to sell web and marketing products
Requirements
Must Have:
- Design must be brickpress compatible, we use the meridian framework specifically.

As a bonus, if we like your work we may use you for our own clients...

Marcus

Industry/Entity Type

Marketing

Requirements
Must have
• For the content area - intro paragraph and blog categories below the header/banner area,

Need to include both shaded content "buttons" with graphics similar to the website attached jpg file titled - bottom content area

and hanging shaded ribbons from pixvault.example - attached jpg file titled: stock-illustration-57310268-glossy-promoting-badges

```html
<!DOCTYPE html>
<html lang="en">
<head>
<meta charset="utf-8">
<title>Frostlane Website Design</title>
<link href="https://fonts.googleapis.com/css2?family=Open+Sans:ital,wght@0,300;0,400;0,600;0,700;1,400&display=swap" rel="stylesheet">
<style>
:root{
  --blue:#1f9fe2;
  --blue-deep:#0b7fd0;
  --blue-light:#45b8f0;
  --yellow:#ffca3a;
  --yellow-deep:#f7b512;
  --orange:#f59a12;
  --red:#c8331f;
  --ink:#444;
  --muted:#8a8a8a;
  --white:#fff;
  --footer-grey:#f1f1f1;
}
*{box-sizing:border-box;margin:0;padding:0}
html,body{width:1200px;height:2732px;overflow:hidden}
body{font-family:"Open Sans",Arial,sans-serif;color:var(--ink);background:var(--white);position:relative}
a{text-decoration:none;color:inherit}

/* Navigation */
.site-nav{position:absolute;top:0;left:0;width:1200px;height:74px;background:var(--white);z-index:3;border-top:4px solid var(--blue)}
.site-nav ul{list-style:none;position:absolute;top:26px;display:flex;gap:48px;font-size:14px;text-transform:uppercase;color:#666}
.site-nav .nav-left{left:160px}
.site-nav .nav-right{left:727px}
.site-nav li.active{color:var(--blue);position:relative}
.site-nav li.active::after{content:"";position:absolute;left:-14px;right:-14px;top:44px;height:4px;background:var(--blue)}
.brand-tab{position:absolute;left:520px;top:-60px;width:160px;height:196px;border-radius:0 0 80px 80px;background:var(--white);z-index:4;display:flex;flex-direction:column;align-items:center;justify-content:flex-end;padding-bottom:34px}
.brand-mark{width:40px;height:40px;border-radius:50%;background:var(--yellow);margin-bottom:8px}
.brand-name{font-size:18px;font-weight:600;letter-spacing:2px;color:#666;text-transform:uppercase}

/* Hero */
.hero{position:absolute;top:74px;left:0;width:1200px;height:396px;background:linear-gradient(180deg,#b9c7cf 0%,#e6d9bf 45%,#f2c25a 75%,#d9a23c 100%)}
.hero-devices{position:absolute;left:260px;top:70px;width:700px;height:300px;border-radius:14px;background:radial-gradient(ellipse at 50% 45%,rgba(255,255,255,.55) 0%,rgba(255,255,255,.25) 45%,rgba(255,255,255,0) 75%)}
.slider-arrow{position:absolute;width:66px;height:66px;border-radius:50%;border:2px solid rgba(255,255,255,.9);background:rgba(0,0,0,.15);display:flex;align-items:center;justify-content:center}

/* Intro */
.intro{position:absolute;top:530px;left:0;width:1200px;text-align:center}
.intro h1{font-size:23px;font-weight:400;color:var(--blue)}
.intro p{width:900px;margin:10px auto 0;font-size:14.5px;line-height:21px;color:var(--muted)}

.service-tiles{position:absolute;top:660px;left:150px;width:900px;display:flex;justify-content:space-between}
.tile{width:283px;height:143px;position:relative;overflow:hidden}
.tile h2{position:absolute;top:10px;width:100%;text-align:center;font-size:22px;font-weight:400;color:var(--white)}
.tile-ecommerce{background:linear-gradient(180deg,#fbb51b 0%,#f8c84a 40%,#f2f0e6 60%,#e7e4da 100%)}
.tile-webdesign{background:linear-gradient(180deg,#f07a12 0%,#f29a2c 40%,#6b4a3a 65%,#a3513e 100%)}
.tile-search{background:linear-gradient(180deg,#1a7fd8 0%,#3aa0ea 45%,#d8e6f2 70%,#eef2f6 100%)}

/* Portfolio */
.portfolio{position:absolute;top:880px;left:0;width:1200px;height:578px;background:radial-gradient(circle at 50% 40%,#ffd65c 0%,var(--yellow) 55%,var(--yellow-deep) 100%);overflow:hidden}
.portfolio h2{position:absolute;top:42px;left:305px;font-size:58px;font-weight:300;color:var(--white);letter-spacing:1px}
.view-all{position:absolute;top:62px;left:800px;padding:6px 16px;background:var(--white);color:var(--red);font-size:17px;font-style:italic;font-weight:700;border-radius:3px;transform:rotate(-4deg)}
.monitor{position:absolute;left:222px;top:130px;width:758px;height:460px;background:#1e1e1e;border-radius:16px;padding:22px 22px 0}
.monitor-screen{width:100%;height:100%;background:#f3e7cf;position:relative;overflow:hidden}
.site-bar{height:30px;background:#6b2f1a;display:flex;align-items:center;font-size:10px;color:#f3d9a8;gap:22px;padding-left:60px}
.site-bar .spacer{width:190px}
.client-name{position:absolute;top:8px;left:300px;width:114px;height:56px;background:#f3e7cf;border-radius:0 0 50px 50px;text-align:center;font-size:13px;font-weight:700;color:#b3261e;padding-top:14px}
.client-address{position:absolute;top:70px;width:100%;text-align:center;font-size:17px;color:#6b2f1a}
.client-photo{position:absolute;top:104px;left:62px;width:588px;height:262px;background:linear-gradient(135deg,#5a2a18 0%,#9a5a2a 45%,#d9b07a 100%);border:6px solid #fff}
.client-tagline{position:absolute;left:0;bottom:0;padding:4px 12px;background:rgba(40,20,10,.55);font-size:14px;color:#fff}
.client-footer-line{position:absolute;top:380px;left:62px;font-size:15px;color:#6b2f1a}

/* About */
.about{position:absolute;top:1490px;left:0;width:1200px}
.about h2{text-align:center;font-size:30px;font-weight:400;color:var(--blue)}
.about .lead{width:880px;margin:16px auto 0;text-align:center;font-size:14px;line-height:21px;color:#666}
.about-columns{position:absolute;top:158px;left:150px;width:900px;display:flex;justify-content:space-between}
.about-columns article{width:425px}
.about-columns h3{font-size:17px;font-weight:400;color:var(--blue);margin-bottom:10px}
.about-columns p{font-size:12px;line-height:19px;color:var(--muted);margin-bottom:14px}

/* Blog & services */
.updates{position:absolute;top:1958px;left:0;width:1200px;height:406px;background:linear-gradient(180deg,var(--blue-light),var(--blue-deep))}
.updates h2{position:absolute;top:44px;font-size:29px;font-weight:400;color:var(--white)}
.blog-title{left:170px}
.services-title{left:858px}
.blog-panel{position:absolute;top:104px;left:150px;width:663px;height:256px;background:#ffe58a;border-radius:10px;padding:24px 28px;display:flex;gap:36px}
.post{width:285px}
.post h3{font-size:11px;font-weight:600;color:#1a6fb0;white-space:nowrap;line-height:16px}
.post .byline{font-size:10px;color:#888;margin:1px 0 10px;line-height:14px}
.post p{font-size:11px;line-height:16px;color:#555}
.read-more{display:block;margin-top:8px;font-size:12px;line-height:16px;font-style:italic;color:var(--red)}
.pager{position:absolute;left:30px;bottom:12px;display:flex;gap:4px}
.pager span{width:10px;height:10px;border-radius:50%;background:#f29a3a}
.pager span:first-child{background:var(--red)}
.services-panel{position:absolute;top:104px;left:831px;width:219px;height:256px;background:rgba(8,75,140,.55);border-radius:10px;padding:28px 22px}
.services-panel ul{list-style:none}
.services-panel li{font-size:11px;font-weight:600;color:var(--white);line-height:21px;display:flex;align-items:center;gap:10px}
.services-panel li::before{content:"";width:8px;height:8px;border-radius:50%;background:var(--white)}

/* Footer */
.site-footer{position:absolute;top:2364px;left:0;width:1200px;height:236px;background:var(--white)}
.site-footer h4{font-size:18px;font-weight:400;color:var(--orange)}
.browse{position:absolute;left:150px;top:34px}
.browse ul{list-style:none;margin-top:18px;font-size:11px;line-height:17px;color:#666}
.testimonial{position:absolute;left:294px;top:34px;width:300px}
.quote-box{margin-top:14px;position:relative;height:120px;background:#f3f3f3;border-radius:10px;padding:14px 14px 0 80px;font-size:11px;line-height:15px;font-style:italic;color:#888}
.avatar{position:absolute;left:-6px;top:18px;width:70px;height:70px;border-radius:50%;background:linear-gradient(135deg,#9fb6c6,#6c7f8c);border:4px solid #fff}
.signature{position:absolute;right:16px;bottom:8px;color:var(--red);font-size:11px}
.contact{position:absolute;left:670px;top:34px;width:200px}
.contact-row{display:flex;align-items:flex-start;gap:10px;margin-top:14px;font-size:11px;line-height:14px;color:#666}
.contact-row strong{color:#444;font-weight:600}
.contact-row .phones{color:var(--orange);font-weight:700;font-size:13px;line-height:17px}
.icon{width:24px;height:24px;flex:none}
.email{color:var(--red)}
.cta{position:absolute;left:876px;top:30px;width:180px;height:150px}
.cta-strip{position:absolute;left:0;top:0;width:26px;height:150px;background:var(--orange);display:flex;align-items:center;justify-content:center}
.cta-strip span{transform:rotate(-90deg);white-space:nowrap;color:var(--white);font-size:12px;font-weight:700;letter-spacing:2px}
.cta-free{position:absolute;left:36px;top:0;font-size:58px;font-weight:600;color:var(--orange);line-height:60px}
.cta-consult{position:absolute;left:38px;top:66px;font-size:19px;line-height:24px;color:var(--orange);letter-spacing:1px}
.cta-phone{position:absolute;left:36px;top:92px;font-size:28px;line-height:36px;color:var(--orange)}

.base-bar{position:absolute;top:2600px;left:0;width:1200px;height:132px;background:var(--footer-grey);text-align:center}
.base-brand{margin-top:30px;display:inline-flex;align-items:center;gap:10px;font-size:17px;font-weight:600;letter-spacing:2px;color:#999;text-transform:uppercase}
.base-brand i{width:30px;height:30px;border-radius:50%;border:3px solid #bbb;display:block}
.base-links{margin-top:22px;font-size:12px;color:#777}
</style>
</head>
<body>

<nav class="site-nav">
  <ul class="nav-left"><li>Home</li><li class="active">About</li><li>Services</li><li>RFQ</li></ul>
  <ul class="nav-right"><li>Portfolio</li><li>Testimonials</li><li>Contact</li></ul>
</nav>
<div class="brand-tab">
  <span class="brand-mark"></span>
  <span class="brand-name">Frostlane</span>
</div>

<section class="hero" role="img" aria-label="Sunlit field backdrop with a desktop, laptop, tablet and phones showing responsive websites">
  <div class="hero-devices"></div>
  <span class="slider-arrow" style="left:150px;top:164px"><svg width="16" height="24"><path d="M12 3 L4 12 L12 21" stroke="#fff" stroke-width="3" fill="none"/></svg></span>
  <span class="slider-arrow" style="left:984px;top:164px"><svg width="16" height="24"><path d="M4 3 L12 12 L4 21" stroke="#fff" stroke-width="3" fill="none"/></svg></span>
</section>

<section class="intro">
  <h1>70% of US households use the internet when searching for local products and services.</h1>
  <p>While most purchases are made offline (67%), they start online at the businesses website. If your website looks unprofessional or cannot be found you are missing out on potential revenue and a steady stream of new customers.</p>
</section>

<section class="service-tiles">
  <div class="tile tile-ecommerce" role="img" aria-label="Ecommerce tile with online shop screenshots"><h2>Ecommerce</h2></div>
  <div class="tile tile-webdesign" role="img" aria-label="Web design tile with fanned website screenshots"><h2>Web Design</h2></div>
  <div class="tile tile-search" role="img" aria-label="Search marketing tile with search result screenshots"><h2>Search Marketing</h2></div>
</section>

<section class="portfolio">
  <h2>OUR PORTFOLIO</h2>
  <a class="view-all">View All</a>
  <span class="slider-arrow" style="left:92px;top:262px;width:58px;height:58px"><svg width="14" height="22"><path d="M11 3 L4 11 L11 19" stroke="#fff" stroke-width="3" fill="none"/></svg></span>
  <span class="slider-arrow" style="left:1050px;top:262px;width:58px;height:58px"><svg width="14" height="22"><path d="M3 3 L10 11 L3 19" stroke="#fff" stroke-width="3" fill="none"/></svg></span>
  <div class="monitor">
    <div class="monitor-screen">
      <div class="site-bar"><span>HOME</span><span>MENUS</span><span>DELIVERY</span><span class="spacer"></span><span>CATERING</span><span>ABOUT US</span><span>CONTACT US</span></div>
      <div class="client-name">Rosalind's</div>
      <div class="client-address">48 Quarry Lane - Millbrook, PA</div>
      <div class="client-photo" role="img" aria-label="Restaurant dish and dining room photo"><span class="client-tagline">serving fresh authentic Italian cuisine</span></div>
      <div class="client-footer-line">Rosalind's Trattoria &amp; Brick Oven</div>
    </div>
  </div>
</section>

<section class="about">
  <h2>Frostlane Website Design - PA</h2>
  <p class="lead">Frostlane, a leading professional web design and web development company operating out of Alder county in northeastern Pennsylvania, serves businesses everywhere from down the street to across the country.</p>
  <div class="about-columns">
    <article>
      <h3>What Makes Frostlane Unique?</h3>
      <p>In a single word...results. Having a website that can't be found is equivalent to putting up a billboard facing away from traffic.</p>
      <p>An attractive site simply isn't enough in today's marketplace. So although many talented graphic designers can construct beautiful sites for pennies on the dollar, very few truly understand the principles of website marketing, copy and design, search engine optimization and legitimate tactics you can use so your website is found by your customers. With Frostlane, you can have it all – an attractive site from talented designers and writers that achieves your business goals.</p>
    </article>
    <article>
      <h3>How Does Frostlane Achieve Results?</h3>
      <p>In a single word...results. Having a website that can't be found is equivalent to putting up a billboard facing away from traffic.</p>
      <p>An attractive site simply isn't enough in today's marketplace. So although many talented graphic designers can construct beautiful sites for pennies on the dollar, very few truly understand the principles of website marketing, copy and design, search engine optimization and legitimate tactics you can use so your website is found by your customers. With Frostlane, you can have it all – an attractive site from talented designers and writers that achieves your business goals.</p>
    </article>
  </div>
</section>

<section class="updates">
  <h2 class="blog-title">Recent Blog Postings</h2>
  <h2 class="services-title">Services</h2>
  <div class="blog-panel">
    <article class="post">
      <h3>Making Your Website Work For You.</h3>
      <div class="byline">by Marcus on May 1, 2013</div>
      <p>Hey! Hope you are having an awesome day! Yesterday I was doing some follow up emails to potential clients that made contact with us sometime ago to see if there might some interest to work with each other yet. This one in particular that I emailed, I noticed that they did have a new website since our last contact and that it definitely did look better from what I remembered.</p>
      <a class="read-more">Read more →</a>
    </article>
    <article class="post">
      <h3>Ridgeway Visitors Bureau Mobile Website Love Today</h3>
      <div class="byline">by Marcus on April 24, 2013</div>
      <p>Hey! Hope you are having an awesome day! Yesterday I was doing some follow up emails to potential clients that made contact with us sometime ago to see if there might some interest to work with each other yet. This one in particular that I emailed, I noticed that they did have a new website since our last contact and that it definitely did look better from what I remembered.</p>
      <a class="read-more">Read more →</a>
    </article>
    <div class="pager"><span></span><span></span><span></span><span></span><span></span></div>
  </div>
  <div class="services-panel">
    <ul>
      <li>Website Design</li><li>Website Re-design</li><li>Ecommerce</li><li>Mobile Websites</li><li>Copywriting</li><li>Hosting and Maintenance</li><li>Content Marketing</li><li>Pay Per Click Marketing</li><li>Mobile Text Marketing</li><li>Local Search Marketing</li>
    </ul>
  </div>
</section>

<footer class="site-footer">
  <div class="browse">
    <h4>Browse Site</h4>
    <ul><li>Frostlane</li><li>Services</li><li>Portfolio</li><li>Contact Us</li><li>Request &amp; Quote</li><li>Associates</li></ul>
  </div>
  <div class="testimonial">
    <h4>Client Testimonials</h4>
    <div class="quote-box">
      <span class="avatar" role="img" aria-label="Client portrait"></span>
      After finding out how hard you worked to develop our website I had to drop you a quick thank you note of true, heart felt thanks from the team and myself. We at The Halden Group are proud to say....
      <span class="signature">C. Rhea Moss</span>
    </div>
  </div>
  <div class="contact">
    <h4>Contact Us</h4>
    <div class="contact-row">
      <svg class="icon" viewBox="0 0 24 24"><circle cx="12" cy="12" r="12" fill="#f59a12"/><path d="M12 5a4.5 4.5 0 0 0-4.5 4.5C7.5 13 12 19 12 19s4.5-6 4.5-9.5A4.5 4.5 0 0 0 12 5z" fill="#fff"/><circle cx="12" cy="9.5" r="1.6" fill="#f59a12"/></svg>
      <div><strong>Frostlane Web Design</strong><br>12 Birch Hollow Road<br>Fernvale, PA 17000</div>
    </div>
    <div class="contact-row">
      <svg class="icon" viewBox="0 0 24 24"><circle cx="12" cy="12" r="12" fill="#f59a12"/><path d="M8 6h2.5l1 3-1.5 1a8 8 0 0 0 3.5 3.5l1-1.5 3 1V16c0 .8-.7 1.5-1.5 1.5A9.5 9.5 0 0 1 6.5 7.5C6.5 6.7 7.2 6 8 6z" fill="#fff"/></svg>
      <div class="phones">(800) 555-0147<br>(570) 555-0192</div>
    </div>
    <div class="contact-row">
      <svg class="icon" viewBox="0 0 24 24"><circle cx="12" cy="12" r="12" fill="#f59a12"/><rect x="6" y="8" width="12" height="8" fill="#fff"/><path d="M6 8l6 4.5L18 8" stroke="#f59a12" stroke-width="1.2" fill="none"/></svg>
      <div class="email">contact@frostlanewd.example</div>
    </div>
  </div>
  <div class="cta">
    <div class="cta-strip"><span>CALL NOW</span></div>
    <div class="cta-free">FREE</div>
    <div class="cta-consult">CONSULTATION</div>
    <div class="cta-phone">570.555.0192</div>
  </div>
</footer>

<div class="base-bar">
  <div class="base-brand"><i></i>Frostlane</div>
  <div class="base-links">Frostlane &nbsp;/&nbsp; Services &nbsp;/&nbsp; Portfolio &nbsp;/&nbsp; Contact Us &nbsp;/&nbsp; Request &amp; Quote &nbsp;/&nbsp; Associates</div>
</div>

</body>
</html>
```